Gift box company needs packaging design for shipping box

We need a design to decorate our brown cardboard shipping boxes. The design must include our company logo (provided) and a "fragile" label somewhere. We will be using single colour printing so the design must only be in one colour. As it will be covering a brown box, I think black or dark blue would be most appropriate. The shipping box itself measures 355mm wide X 246mm deep X 105mm tall. If the design could make the box look like a wrapped present in some way, that would be great.

```html
<!DOCTYPE html>
<html lang="en">
<head>
<meta charset="utf-8">
<title>Kindly Wrapped – Shipping Box Artwork</title>
<link href="https://fonts.googleapis.com/css2?family=Oswald:wght@500;700&display=swap" rel="stylesheet">
<style>
  :root {
    --stage: #ededed;
    --kraft: #cfb08a;
    --kraft-edge: #b89772;
    --ink: #111111;
    --ornament: #2a2623;
  }
  * { box-sizing: border-box; margin: 0; padding: 0; }
  html, body { width: 1200px; height: 1200px; overflow: hidden; background: var(--stage); }
  .artwork {
    position: relative; width: 1200px; height: 1200px;
    font-family: "Oswald", "Arial Narrow", sans-serif; color: var(--ink);
  }
  .panel {
    position: absolute; background: var(--kraft);
    border: 2px solid var(--kraft-edge); overflow: hidden;
  }
  .panel-top { left: 245px; top: 60px; width: 710px; height: 492px; }
  .panel-long { left: 245px; top: 572px; width: 710px; height: 240px; }
  .panel-short { left: 354px; top: 832px; width: 492px; height: 240px; }

  .flap-seam {
    position: absolute; left: 0; right: 0; top: 245px; height: 2px; background: var(--kraft-edge);
  }

  .logo-frame {
    position: absolute; display: flex; align-items: center; justify-content: center;
  }
  .logo-frame .frame-line { position: absolute; inset: 22px; border: 1.5px solid var(--ink); }
  .ornament {
    position: absolute; width: 40px; height: 28px; background: var(--ornament); border-radius: 40%;
  }
  .ornament.tl { left: 2px; top: 8px; }
  .ornament.tr { right: 2px; top: 8px; }
  .ornament.bl { left: 2px; bottom: 8px; }
  .ornament.br { right: 2px; bottom: 8px; }
  .brand-name {
    position: relative; font-weight: 500; font-size: 30px; letter-spacing: 3px;
    text-transform: uppercase; text-align: center; line-height: 1.05;
  }

  .top-logo { width: 420px; height: 180px; left: 145px; }
  .top-logo.upper { top: 32px; transform: rotate(180deg); }
  .top-logo.lower { top: 280px; }

  .ribbon-band { position: absolute; left: 0; right: 0; top: 96px; height: 44px; background: var(--ink); }

  .bow {
    position: absolute; left: 120px; top: 40px; width: 190px; height: 170px;
    background: var(--ink); border-radius: 8px;
  }
  .side-logo { width: 290px; height: 210px; right: 40px; top: 15px; background: var(--kraft); }

  .fragile-label {
    position: absolute; border: 3px solid var(--ink); outline: 1.5px solid var(--ink);
    outline-offset: 3px; background: var(--kraft); font-weight: 700;
    text-transform: uppercase; line-height: 1; padding: 6px 10px;
  }
  .panel-short .fragile-label { left: 170px; top: 80px; font-size: 48px; transform: rotate(-2deg); }
  .panel-long .fragile-label.small { left: 22px; top: 186px; font-size: 24px; padding: 3px 6px; outline: none; }

  .up-arrow { position: absolute; }
  .handling-icons {
    position: absolute; left: 22px; top: 156px; display: grid;
    grid-template-columns: 30px 30px; gap: 6px;
  }
  .handling-icons svg { width: 30px; height: 30px; border: 2px solid var(--ink); }
  .crop-mark { position: absolute; width: 16px; height: 16px; border-color: var(--ink); border-style: solid; border-width: 0; }
  .crop-mark.tl { left: 100px; top: 160px; border-top-width: 4px; border-left-width: 4px; }
  .crop-mark.tr { left: 190px; top: 160px; border-top-width: 4px; border-right-width: 4px; }
  .crop-mark.bl { left: 100px; top: 212px; border-bottom-width: 4px; border-left-width: 4px; }
  .crop-mark.br { left: 190px; top: 212px; border-bottom-width: 4px; border-right-width: 4px; }
</style>
</head>
<body>
<main class="artwork">

  <section class="panel panel-top" aria-label="Lid">
    <div class="logo-frame top-logo upper">
      <span class="frame-line"></span>
      <span class="ornament tl" role="img" aria-label="Floral corner ornament"></span>
      <span class="ornament tr" role="img" aria-label="Floral corner ornament"></span>
      <span class="ornament bl" role="img" aria-label="Floral corner ornament"></span>
      <span class="ornament br" role="img" aria-label="Floral corner ornament"></span>
      <span class="brand-name">Kindly Wrapped</span>
    </div>
    <div class="flap-seam"></div>
    <div class="logo-frame top-logo lower">
      <span class="frame-line"></span>
      <span class="ornament tl" role="img" aria-label="Floral corner ornament"></span>
      <span class="ornament tr" role="img" aria-label="Floral corner ornament"></span>
      <span class="ornament bl" role="img" aria-label="Floral corner ornament"></span>
      <span class="ornament br" role="img" aria-label="Floral corner ornament"></span>
      <span class="brand-name">Kindly Wrapped</span>
    </div>
  </section>

  <section class="panel panel-long" aria-label="Long side">
    <div class="ribbon-band"></div>
    <svg class="up-arrow" style="left:30px;top:40px" width="60" height="34" viewBox="0 0 60 34">
      <polygon points="30,0 60,16 44,16 44,34 16,34 16,16 0,16" fill="#111"/>
    </svg>
    <div class="bow" role="img" aria-label="Ribbon bow illustration tied on the band"></div>
    <div class="logo-frame side-logo">
      <span class="frame-line"></span>
      <span class="ornament tl" role="img" aria-label="Floral corner ornament"></span>
      <span class="ornament tr" role="img" aria-label="Floral corner ornament"></span>
      <span class="ornament bl" role="img" aria-label="Floral corner ornament"></span>
      <span class="ornament br" role="img" aria-label="Floral corner ornament"></span>
      <span class="brand-name">Kindly<br>Wrapped</span>
    </div>
    <div class="fragile-label small">Fragile</div>
  </section>

  <section class="panel panel-short" aria-label="Short side">
    <div class="ribbon-band"></div>
    <svg class="up-arrow" style="left:206px;top:14px" width="80" height="46" viewBox="0 0 80 46">
      <polygon points="40,0 80,22 58,22 58,46 22,46 22,22 0,22" fill="#111"/>
    </svg>
    <div class="fragile-label">Fragile</div>
    <div class="handling-icons" aria-label="Handling symbols">
      <svg viewBox="0 0 30 30"><path d="M9 22 Q15 12 21 22 M15 8 v6" stroke="#111" stroke-width="2" fill="none"/></svg>
      <svg viewBox="0 0 30 30"><path d="M10 24V8M6 12l4-5 4 5M20 24V8M16 12l4-5 4 5" stroke="#111" stroke-width="2" fill="none"/></svg>
      <svg viewBox="0 0 30 30"><path d="M9 6h12l-2 10h-8z M15 16v8 M10 24h10" stroke="#111" stroke-width="2" fill="none"/></svg>
      <svg viewBox="0 0 30 30"><path d="M5 15a10 8 0 0 1 20 0z M15 15v8a2 2 0 0 1-4 0" stroke="#111" stroke-width="2" fill="#111"/></svg>
    </div>
    <span class="crop-mark tl"></span><span class="crop-mark tr"></span>
    <span class="crop-mark bl"></span><span class="crop-mark br"></span>
  </section>

</main>
</body>
</html>
```